Design a cover that embodies the concept of healing by Walking Out of Sorrow

Subtitle: How to use tapping, applied kinesiology, and Chinese medicine to heal your body, free your mind and live in peace.

Tapping (Emotional Freedom Technique) is a modern mix of psychology and Chinese medicine that helps people to release the emotions they have inside that are contributing to the depression and anxiety they feel. Applied kinesiology or muscle testing is a biofeedback tool which helps to extract information from the body that can help people to profoundly heal. It can be used to determine whether heavy metals, heavy chemicals, food sensitivities or pathogens are causing the body problems. It can also be used to determine which supplements can help someone heal. This tool also can be used to identify emotions and memories that are also causing someone problems. Lastly, Chinese medicine uses food therapy, herbal formulas, meditation, tai chi (meditative movement), cupping and other tools to help people to be free of depression. This book is written to be information but also details my own personal journey of how I was able to heal from 11 years of heavy depression through the use of these tools.

The heart of the book is about emotional release, emotional freedom and emotional healing. You can surrender, release or let go of emotions and feel better very quickly. This certainly was my experience.

I would like the front and back cover to each be 8.5" x 5.5". I still have to get an ISBN number for the back page as well. Here is the text that I would like on the back cover for now: Millions of people feel the pain, loneliness, and agony of anxiety and depression every day. Many turn to Western medicine in the hopes that a pill will ease the pain and make the problem go away. Oftentimes, this only makes matters worse and doesn’t address the root cause. No one should have to struggle like this when natural answers exist that can address the physical, energetic, emotional, or spiritual causes of anxiety and depression. For 11 long years, Dr. Neil personally struggled with heavy depression until he discovered answers that helped him to completely heal. Walking Out of Sorrow is a guide that will help you discover - The two root physical causes of depression and exactly what to do to start healing today - How the negative emotions we have stored within from trauma and bad experiences can drive depression - Tools from Chinese medicine, applied kinesiology, and tapping to help you free your mind and live in peace - An actionable plan to help you let go of the pain, suffering, and negative emotions from your past Whether you feel depressed and anxious or know someone who struggles with these issues, Walking Out of Sorrow will transform how you think about depression and will give you the tools to heal so that you can be free and live in peace. Dr. Neil Prentor is a board-certified acupuncture physician licensed in the state of Florida. He received his training at the Marlow Institute of Holistic Practice. He also graduated with a master’s degree in counseling and psychology from Ashcombe Seminary of Theology. His mission is to help people transform their health and improve the quality of their life naturally. He lives in Orlando, FL where he runs a holistic medical clinic called Kestrel Wellness Center. www.drneilprentor.example Instagram: drneilprentor Facebook: kestrelwellnesscenter

Target Market(s)

Those who suffer from depression and anxiety and want to heal naturally

Industry/Entity Type

Health And Wellness

Requirements
Must have
• My picture should be small and go on the back cover next to the information about me. The front cover would be all graphical. Thank you. On the front cover my name should be posted as "Dr. Neil Prentor, AP, MA"

```html
<!DOCTYPE html>
<html lang="en">
<head>
<meta charset="utf-8">
<title>Walking Out of Sorrow – Cover Spread</title>
<link rel="stylesheet" href="https://fonts.googleapis.com/css2?family=Mulish:wght@300;400;600;700;800&family=Kaushan+Script&display=swap">
<style>
  :root {
    --page-bg: #ffffff;
    --cover-blue: #2b3f96;
    --cover-blue-deep: #23357f;
    --cover-blue-light: #3550a8;
    --accent-orange: #e08a1e;
    --text-white: #ffffff;
    --text-soft: #e9ecf7;
    --spine-line: #8a9bd6;
    --art-orange: #f08a2c;
    --art-green: #6cc07a;
    --art-teal: #2f8fc0;
    --art-blue: #2a5fb5;
  }
  * { box-sizing: border-box; margin: 0; padding: 0; }
  html, body { width: 800px; height: 1200px; overflow: hidden; background: var(--page-bg); }
  .canvas { position: relative; width: 800px; height: 1200px; }

  .spread {
    position: absolute; left: 20px; top: 318px;
    width: 1360px; height: 1010px;
    transform: scale(0.5588); transform-origin: 0 0;
    display: flex;
    font-family: "Mulish", sans-serif;
    color: var(--text-white);
  }
  .panel {
    position: relative; height: 100%; overflow: hidden;
    background:
      radial-gradient(ellipse at 30% 70%, var(--cover-blue-light) 0%, transparent 55%),
      radial-gradient(ellipse at 80% 20%, var(--cover-blue-deep) 0%, transparent 60%),
      var(--cover-blue);
  }
  .back-cover { width: 655px; }
  .spine { width: 50px; border-left: 2px solid var(--spine-line); border-right: 2px solid var(--spine-line); }
  .front-cover { width: 655px; }

  .cover-art { position: absolute; left: 0; top: 0; }

  .script-title { font-family: "Kaushan Script", cursive; color: var(--accent-orange); font-weight: 400; }
  .main-title { font-weight: 800; letter-spacing: 1px; color: var(--text-white); line-height: 1; }

  /* back cover */
  .author-photo { position: absolute; left: 330px; top: 68px; width: 136px; height: 136px; border-radius: 50%;
    background: radial-gradient(circle at 50% 45%, #d9a98a 0%, #a77a5e 40%, #7f8f6a 75%, #b9c39a 100%); }
  .back-author { position: absolute; left: 312px; top: 212px; font-size: 13px; font-weight: 400; letter-spacing: .3px; }
  .back-title { position: absolute; left: 100px; top: 242px; width: 455px; text-align: right; }
  .back-title .script-title { font-size: 40px; display: block; margin-right: 10px; }
  .back-title .main-title { font-size: 66px; text-align: center; margin-top: -14px; }
  .blurb {
    position: absolute; left: 100px; top: 360px; width: 453px; height: 420px;
    columns: 2; column-gap: 20px; column-fill: auto;
    font-size: 12.2px; line-height: 15.7px; font-weight: 300; text-align: justify; color: var(--text-soft);
  }
  .contact { position: absolute; left: 200px; top: 788px; width: 260px; text-align: center; font-size: 12px; line-height: 18px; }
  .contact b { color: var(--accent-orange); font-weight: 700; }
  .isbn-box { position: absolute; left: 337px; top: 862px; width: 225px; height: 120px; background: var(--text-white); }

  /* spine */
  .spine-text { position: absolute; left: 0; top: 0; width: 50px; height: 100%;
    writing-mode: vertical-rl; transform: rotate(180deg);
    display: flex; align-items: center; justify-content: flex-start; gap: 24px; padding: 150px 0 170px; }
  .spine-author { font-size: 20px; font-weight: 700; letter-spacing: .5px; }
  .spine-title { font-size: 38px; font-weight: 800; letter-spacing: 1px; }
  .spine-script { font-family: "Kaushan Script", cursive; color: var(--accent-orange); font-size: 20px; }

  /* front cover */
  .front-title { position: absolute; left: 25px; top: 638px; width: 605px; text-align: center; }
  .front-title .script-title { display: block; font-size: 58px; text-align: right; padding-right: 20px; }
  .front-title .main-title { font-size: 92px; margin-top: -20px; }
  .subtitle { position: absolute; left: 60px; top: 822px; width: 535px; text-align: center;
    color: var(--accent-orange); font-size: 23px; line-height: 31px; font-weight: 400; }
  .front-author { position: absolute; left: 0; top: 952px; width: 655px; text-align: center; font-size: 19px; font-weight: 700; letter-spacing: .5px; }
</style>
</head>
<body>
<div class="canvas">
  <div class="spread">

    <section class="panel back-cover">
      <svg class="cover-art" width="655" height="300" viewBox="0 0 655 300">
        <defs>
          <radialGradient id="art-back" cx="35%" cy="30%" r="75%">
            <stop offset="0" stop-color="var(--art-orange)"/>
            <stop offset=".35" stop-color="var(--art-green)"/>
            <stop offset=".7" stop-color="var(--art-teal)"/>
            <stop offset="1" stop-color="var(--art-blue)"/>
          </radialGradient>
        </defs>
        <circle cx="125" cy="110" r="150" fill="url(#art-back)" role="img" aria-label="Abstract fluid-paint artwork of an embracing figure"/>
        <path d="M0,262 Q170,285 270,205 Q330,160 355,110" fill="none" stroke="var(--accent-orange)" stroke-width="9" stroke-linecap="round"/>
        <path d="M318,0 Q345,20 362,55" fill="none" stroke="var(--accent-orange)" stroke-width="2"/>
      </svg>
      <div class="author-photo" role="img" aria-label="Portrait of the author"></div>
      <p class="back-author">DR. NEIL PRENTOR, AP, MA</p>
      <h2 class="back-title">
        <span class="script-title">Walking out of</span>
        <span class="main-title">SORROW</span>
      </h2>
      <div class="blurb">
        <p>Millions of people feel the pain, loneliness, and agony of anxiety and depression every day. Many turn to Western medicine in the hopes that a pill will ease the pain and make the problem go away. Oftentimes, this only makes matters worse and doesn’t address the root cause. No one should have to struggle like this when natural answers exist that can address the physical, energetic, emotional, or spiritual causes of anxiety and depression. For 11 long years, Dr. Neil personally struggled with heavy depression until he discovered answers that helped him to completely heal.</p>
        <p>Walking Out of Sorrow is a guide that will help you discover - The two root physical causes of depression and exactly what to do to start healing today - How the negative emotions we have stored within from trauma and bad experiences can drive depression - Tools from Chinese medicine, applied kinesiology, and tapping to help you free your mind and live in peace - An actionable plan to help you let go of the pain, suffering, and negative emotions from your past Whether you feel depressed and anxious or know someone who struggles with these issues, Walking Out of Sorrow will transform how you think about depression and will give you the tools to heal so that you can be free and live in peace.</p>
        <p>Dr. Neil Prentor is a board-certified acupuncture physician licensed in the state of Florida. He received his training at the Marlow Institute of Holistic Practice. He also graduated with a master’s degree in counseling and psychology from Ashcombe Seminary of Theology. His mission is to help people transform their health and improve the quality of their life naturally. He lives in Orlando, FL where he runs a holistic medical clinic called Kestrel Wellness Center.</p>
      </div>
      <div class="contact">
        <b>www.drneilprentor.example</b><br>
        <b>Instagram</b> drneilprentor<br>
        <b>Facebook</b> kestrelwellnesscenter
      </div>
      <div class="isbn-box"></div>
    </section>

    <section class="panel spine">
      <div class="spine-text">
        <span class="spine-author">DR. NEIL PRENTOR</span>
        <span class="spine-title">SORROW</span>
        <span class="spine-script">Walking out of</span>
      </div>
    </section>

    <section class="panel front-cover">
      <svg class="cover-art" width="655" height="680" viewBox="0 0 655 680">
        <defs>
          <radialGradient id="art-front" cx="35%" cy="25%" r="80%">
            <stop offset="0" stop-color="var(--art-orange)"/>
            <stop offset=".3" stop-color="var(--art-green)"/>
            <stop offset=".65" stop-color="var(--art-teal)"/>
            <stop offset="1" stop-color="var(--art-blue)"/>
          </radialGradient>
        </defs>
        <circle cx="320" cy="265" r="325" fill="url(#art-front)" role="img" aria-label="Abstract fluid-paint artwork of an embracing figure"/>
        <path d="M0,630 Q260,680 480,560 Q590,495 640,395" fill="none" stroke="var(--accent-orange)" stroke-width="16" stroke-linecap="round"/>
      </svg>
      <h1 class="front-title">
        <span class="script-title">Walking out of</span>
        <span class="main-title">SORROW</span>
      </h1>
      <p class="subtitle">How to use tapping, applied kinesiology, and Chinese medicine to heal your body, free your mind and live in peace.</p>
      <p class="front-author">DR. NEIL PRENTOR, AP, MA</p>
    </section>

  </div>
</div>
</body>
</html>
```